Mobile Oil Change company needs a flyer to promote new business

We need a flyer to 1) print & handout and 2) email out to potential customers. We are a mobile oil change company that comes to our customer locations to perform the work instead of customers going to traditional oil change companies. We have a 21 point inspection with our oil change. (21 point inspection details will not be on the flyer). Would like to keep the flyer simple but creative. I'm attaching 1) the write-up we created, 2) our logo (logo color is dark teal on white but other combinations are included if you wanted to propose a different color combination), and 3) additional services we offer. Logo font is Alegreya Sans.
Would like the additional services listed with icons and brief descriptions (similar to attachment) without pricing. Company website for reference is www.brindlefleetcare.com.

Target Market(s)

Companies with many service vehicles such as Oil & Gas service companies, heating and air conditioning companies, utility companies, police departments, etc. Companies that prioritize convenience and maintenance first.

Font styles to use
Sans Serif

Colors
00a990

Requirements
Must have
• Simple but creative design with our logo at top of the flyer. Additional Services (details in document supplied) can be smaller and less prominent than other "main" content listed in the CONTENT document supplied.
Should not have
• Do not use animated character graphics in the flyer and limit (1) stock photos to A small area in the flyer.

```html
<!DOCTYPE html>
<html lang="en">
<head>
<meta charset="utf-8">
<title>Brindle Fleet Care – Hassle Free Oil Changes</title>
<link href="https://fonts.googleapis.com/css2?family=Alegreya+Sans:wght@700;800&family=Poppins:wght@400;500;600;700&family=Dancing+Script:wght@700&display=swap" rel="stylesheet">
<style>
  :root {
    --teal: #00a990;
    --teal-dark: #0e5d59;
    --teal-deep: #0a4845;
    --teal-mid: #13706a;
    --teal-soft: #3fb8a3;
    --orange: #f26b2a;
    --white: #ffffff;
    --ink: #1f3b3a;
  }
  * { margin: 0; padding: 0; box-sizing: border-box; }
  html, body { width: 851px; height: 1200px; overflow: hidden; background: var(--white); }
  .flyer {
    position: relative; width: 851px; height: 1200px; overflow: hidden;
    background: var(--white); font-family: "Poppins", Arial, sans-serif; color: var(--ink);
  }
  .hero-art {
    position: absolute; left: 400px; top: 20px; width: 440px; height: 520px;
    border-radius: 24px;
    background: radial-gradient(ellipse at 70% 55%, #f7d3c8 0%, #eaf4f2 60%, #ffffff 100%);
  }
  .brand {
    position: absolute; left: 56px; top: 70px; z-index: 2;
    display: flex; align-items: center; gap: 10px;
    font-family: "Alegreya Sans", Arial, sans-serif; font-weight: 800;
    font-size: 31px; color: var(--teal-dark); letter-spacing: 0.3px; white-space: nowrap;
  }
  .brand-mark { width: 18px; height: 18px; background: var(--teal); border-radius: 50%; }
  .headline { position: absolute; left: 62px; top: 290px; z-index: 2; }
  .headline-lead { font-size: 40px; font-weight: 500; color: var(--teal-dark); line-height: 1; }
  .headline-script {
    font-family: "Dancing Script", cursive; font-size: 88px; color: var(--teal-dark);
    line-height: 1; margin-top: 6px; white-space: nowrap;
  }
  .headline-tail { font-size: 32px; font-weight: 500; color: var(--orange); margin-top: 6px; }
  .wave { position: absolute; left: 0; top: 520px; width: 851px; height: 680px; }
  .process-title {
    position: absolute; top: 670px; width: 100%; text-align: center;
    color: var(--white); font-size: 34px; font-weight: 500;
  }
  .process-sub {
    position: absolute; top: 722px; left: 0; width: 100%; text-align: center;
    color: var(--white); font-size: 18px; line-height: 1.35;
  }
  .steps { position: absolute; left: 44px; top: 790px; width: 390px; list-style: none; }
  .step { display: flex; align-items: center; gap: 18px; height: 68px; }
  .step-icon {
    flex: 0 0 52px; height: 52px; border-radius: 50%; background: var(--teal-mid);
    display: flex; align-items: center; justify-content: center;
  }
  .step-text { color: var(--white); font-size: 16px; font-style: italic; line-height: 1.3; }
  .perks { position: absolute; left: 458px; top: 795px; width: 350px; list-style: none; }
  .perk { display: flex; gap: 12px; color: var(--white); font-size: 16px; line-height: 1.35; margin-bottom: 14px; }
  .perk svg { flex: 0 0 24px; margin-top: 0; }
  .contact-card {
    position: absolute; left: 455px; top: 950px; width: 355px; height: 140px;
    background: var(--white); border-radius: 14px; padding: 16px 20px;
    display: flex; flex-direction: column; align-items: center; justify-content: center;
  }
  .contact-mark { width: 28px; height: 28px; background: var(--teal); border-radius: 6px; margin-bottom: 10px; }
  .contact-phone { font-size: 26px; font-weight: 700; color: var(--teal-deep); white-space: nowrap; }
  .contact-email { font-size: 15px; color: var(--teal-deep); margin-top: 2px; }
  .footer {
    position: absolute; left: 0; bottom: 0; width: 100%; height: 34px;
    background: var(--teal); display: flex; justify-content: space-between; align-items: center;
    padding: 0 50px; color: var(--white); font-size: 15px;
  }
</style>
</head>
<body>
<div class="flyer">
  <div class="hero-art" role="img" aria-label="Illustration of a mechanic pouring oil beside a red car with its hood open"></div>

  <div class="brand"><span class="brand-mark"></span>Brindle Fleet Care</div>

  <div class="headline">
    <p class="headline-lead">Hassle Free</p>
    <p class="headline-script">Oil Changes</p>
    <p class="headline-tail">On Your Terms</p>
  </div>

  <svg class="wave" viewBox="0 0 851 680" preserveAspectRatio="none" aria-hidden="true">
    <path d="M0 20 C220 20 330 60 500 100 C650 135 760 120 851 80 L851 680 L0 680 Z" fill="var(--teal-soft)"/>
    <path d="M0 70 C200 60 340 100 500 135 C650 165 760 150 851 115 L851 680 L0 680 Z" fill="var(--teal-dark)"/>
  </svg>

  <h2 class="process-title">Our simple 5-step process</h2>
  <p class="process-sub">lets you schedule an appointment and get service to save time<br>and money:</p>

  <ul class="steps">
    <li class="step">
      <span class="step-icon"><svg width="26" height="26" viewBox="0 0 24 24" fill="none" stroke="#fff" stroke-width="2" stroke-linecap="round" stroke-linejoin="round"><path d="M22 16.9v3a2 2 0 0 1-2.2 2 19.8 19.8 0 0 1-8.6-3.1 19.5 19.5 0 0 1-6-6A19.8 19.8 0 0 1 2.1 4.2 2 2 0 0 1 4.1 2h3a2 2 0 0 1 2 1.7c.1.9.4 1.8.7 2.7a2 2 0 0 1-.5 2.1L8 9.8a16 16 0 0 0 6 6l1.3-1.3a2 2 0 0 1 2.1-.4c.9.3 1.8.6 2.7.7a2 2 0 0 1 1.7 2z"/></svg></span>
      <span class="step-text">Call or email us to schedule service</span>
    </li>
    <li class="step">
      <span class="step-icon"><svg width="26" height="26" viewBox="0 0 24 24" fill="none" stroke="#fff" stroke-width="2" stroke-linecap="round"><circle cx="12" cy="8" r="4"/><path d="M4 21c0-4 3.6-7 8-7s8 3 8 7"/></svg></span>
      <span class="step-text">Our highly trained technicians come to you for service</span>
    </li>
    <li class="step">
      <span class="step-icon"><svg width="26" height="26" viewBox="0 0 24 24" fill="none" stroke="#fff" stroke-width="2" stroke-linecap="round" stroke-linejoin="round"><path d="M14.7 6.3a4 4 0 0 0 5 5L21 13l-8 8-3-3 8-8-1.3-1.3a4 4 0 0 1-5-5z"/><path d="M3 21l6-6"/></svg></span>
      <span class="step-text">Service is performed quickly on your vehicle</span>
    </li>
    <li class="step">
      <span class="step-icon"><svg width="26" height="26" viewBox="0 0 24 24" fill="none" stroke="#fff" stroke-width="2" stroke-linecap="round"><rect x="2" y="5" width="20" height="14" rx="2"/><path d="M2 10h20M6 15h4"/></svg></span>
      <span class="step-text">Pay agreed-upon pricing and receipt is emailed to you</span>
    </li>
    <li class="step">
      <span class="step-icon"><svg width="26" height="26" viewBox="0 0 24 24" fill="none" stroke="#fff" stroke-width="2" stroke-linecap="round" stroke-linejoin="round"><rect x="5" y="3" width="14" height="18" rx="2"/><path d="M9 9l1.5 1.5L14 7M9 15h6"/></svg></span>
      <span class="step-text">Services performed are tracked electronically and reminders created</span>
    </li>
  </ul>

  <ul class="perks">
    <li class="perk"><svg width="24" height="24" viewBox="0 0 24 24" fill="none" stroke="#fff" stroke-width="1.8" stroke-linecap="round" stroke-linejoin="round"><circle cx="12" cy="12" r="10"/><path d="M7.5 12.5l3 3 6-6.5"/></svg>High quality synthetic oil used is best suited for commercial vehicles</li>
    <li class="perk"><svg width="24" height="24" viewBox="0 0 24 24" fill="none" stroke="#fff" stroke-width="1.8" stroke-linecap="round" stroke-linejoin="round"><circle cx="12" cy="12" r="10"/><path d="M7.5 12.5l3 3 6-6.5"/></svg>Service includes a 21-point inspection</li>
    <li class="perk"><svg width="24" height="24" viewBox="0 0 24 24" fill="none" stroke="#fff" stroke-width="1.8" stroke-linecap="round" stroke-linejoin="round"><circle cx="12" cy="12" r="10"/><path d="M7.5 12.5l3 3 6-6.5"/></svg>Additional services are available</li>
  </ul>

  <div class="contact-card">
    <span class="contact-mark"></span>
    <p class="contact-phone">Call: (833) 555-0142</p>
    <p class="contact-email">E.Sales@BrindleFleetCare.com</p>
  </div>

  <footer class="footer">
    <span>www.brindlefleetcare.com</span>
    <span>sales@brindlefleetcare.com</span>
  </footer>
</div>
</body>
</html>
```